24 Hour Fitness Center Store front. Window advertisment

We need a signage design for a 24 hour fitness center in Central FL. Bold Pace Fitness. I have attached photos that show our store front. The signage will cover 4 windows from the far left side towards the right, and 3 windows from the far right towards the left. So 7 windows total. The middle windows including the doors will be blank for customers to see inside.
We want to portray "Results" when people walk up. Our colors are shown on our Logo (attached). Red, gray, black. We are open to any ideas and concepts as far as how the layout is shown, example: Each window a different image, or one large image on each side shown through all windows. I have also attached some examples of other stores that look appealing. Our Services include 24 hour access, personal training, tanning, and group exercise. Each window is approximately 60 inches wide and 75 inches tall.
Thank you!

```html
<!DOCTYPE html>
<html lang="en">
<head>
<meta charset="utf-8">
<title>Bold Pace Fitness – Results Window Signage</title>
<link rel="stylesheet" href="https://fonts.googleapis.com/css2?family=Montserrat:wght@900&family=Arimo:wght@400;700&display=swap">
<style>
  :root {
    --paper: #ffffff;
    --frame: #9a9a9a;
    --panel-line: #2b2b2b;
    --brand-red: #e0301e;
    --brand-gray: #3a3a3a;
    --shadow: rgba(0, 0, 0, 0.28);
  }
  html, body {
    margin: 0;
    padding: 0;
    width: 1200px;
    height: 733px;
    overflow: hidden;
    background: var(--paper);
  }
  .board {
    position: absolute;
    left: 10px;
    top: 10px;
    width: 1178px;
    height: 704px;
    border: 1px solid var(--frame);
    box-shadow: 5px 5px 6px var(--shadow);
    background: var(--paper);
  }
  .window {
    position: absolute;
    border: 1px solid var(--panel-line);
    background: var(--paper);
    box-sizing: border-box;
  }
  .window svg { position: absolute; inset: 0; width: 100%; height: 100%; }
  .window--large { top: 25px; width: 370px; height: 462px; }
  .window--small { top: 502px; width: 158px; height: 197px; }
  .letter {
    font-family: "Montserrat", "Arial Black", sans-serif;
    font-weight: 900;
  }
  .services {
    position: absolute;
    left: 0;
    right: 0;
    top: 377px;
    text-align: center;
    font-family: "Arimo", Arial, sans-serif;
    font-size: 8px;
    color: var(--brand-red);
  }
  .brand {
    position: absolute;
    display: flex;
    align-items: center;
    font-family: "Arimo", Arial, sans-serif;
    font-weight: 700;
    color: var(--brand-gray);
    white-space: nowrap;
  }
  .brand__dot { border-radius: 50%; background: var(--brand-red); }
  .window--large .brand { right: 22px; top: 422px; font-size: 10px; gap: 4px; }
  .window--large .brand__dot { width: 9px; height: 9px; }
  .window--small .brand { right: 10px; top: 178px; font-size: 5px; gap: 2px; }
  .window--small .brand__dot { width: 5px; height: 5px; }
  .rule {
    position: absolute;
    left: 30px;
    width: 101px;
    top: 160px;
    height: 1px;
    background: var(--brand-red);
  }
</style>
</head>
<body>
<svg width="0" height="0" style="position:absolute" aria-hidden="true">
  <defs>
    <linearGradient id="tone-group" x1="0" y1="0" x2="1" y2="1">
      <stop offset="0" stop-color="#5b9fd6"/><stop offset="0.35" stop-color="#e7b48f"/>
      <stop offset="0.6" stop-color="#20a9a6"/><stop offset="0.8" stop-color="#e3366e"/><stop offset="1" stop-color="#2a2420"/>
    </linearGradient>
    <linearGradient id="tone-weights" x1="0" y1="0" x2="1" y2="1">
      <stop offset="0" stop-color="#d9dbdd"/><stop offset="0.4" stop-color="#4a3a32"/>
      <stop offset="0.7" stop-color="#9da3a8"/><stop offset="1" stop-color="#5a4b8a"/>
    </linearGradient>
    <linearGradient id="tone-cycling" x1="0" y1="0" x2="1" y2="1">
      <stop offset="0" stop-color="#c9a27f"/><stop offset="0.45" stop-color="#e8e6e1"/>
      <stop offset="0.75" stop-color="#5c6670"/><stop offset="1" stop-color="#1f2428"/>
    </linearGradient>
    <linearGradient id="tone-kettlebell" x1="0" y1="0" x2="1" y2="1">
      <stop offset="0" stop-color="#7fb6e6"/><stop offset="0.5" stop-color="#c78a66"/>
      <stop offset="0.8" stop-color="#35b07a"/><stop offset="1" stop-color="#1b1b1b"/>
    </linearGradient>
    <linearGradient id="tone-treadmill" x1="0" y1="0" x2="1" y2="1">
      <stop offset="0" stop-color="#c9cbcd"/><stop offset="0.45" stop-color="#d2453a"/>
      <stop offset="1" stop-color="#3a3d40"/>
    </linearGradient>
    <linearGradient id="tone-friends" x1="0" y1="0" x2="1" y2="1">
      <stop offset="0" stop-color="#7cc4a0"/><stop offset="0.4" stop-color="#d98f76"/>
      <stop offset="0.7" stop-color="#c33f8c"/><stop offset="1" stop-color="#6a4f9a"/>
    </linearGradient>
    <linearGradient id="tone-trainer" x1="0" y1="0" x2="1" y2="1">
      <stop offset="0" stop-color="#b9d3e6"/><stop offset="0.45" stop-color="#c48a6a"/>
      <stop offset="1" stop-color="#202326"/>
    </linearGradient>
  </defs>
</svg>

<div class="board"></div>

<!-- Large windows -->
<section class="window window--large" style="left:27px">
  <svg viewBox="0 0 370 462"><text class="letter" x="71" y="346" font-size="318" textLength="227" lengthAdjust="spacingAndGlyphs" fill="url(#tone-group)" role="img" aria-label="Letter R filled with a photo of women in a group exercise class">R</text></svg>
  <p class="services">24 Hour Access | Personal Training | Tanning | Group Exercise</p>
  <div class="brand"><span class="brand__dot"></span>Bold Pace Fitness</div>
</section>
<section class="window window--large" style="left:412px">
  <svg viewBox="0 0 370 462"><text class="letter" x="88" y="346" font-size="318" textLength="194" lengthAdjust="spacingAndGlyphs" fill="url(#tone-weights)" role="img" aria-label="Letter E filled with a photo of a man lifting dumbbells in a gym">E</text></svg>
  <p class="services">24 Hour Access | Personal Training | Tanning | Group Exercise</p>
  <div class="brand"><span class="brand__dot"></span>Bold Pace Fitness</div>
</section>
<section class="window window--large" style="left:797px">
  <svg viewBox="0 0 370 462"><text class="letter" x="80" y="346" font-size="318" textLength="214" lengthAdjust="spacingAndGlyphs" fill="url(#tone-cycling)" role="img" aria-label="Letter S filled with a photo of a spin cycling class">S</text></svg>
  <p class="services">24 Hour Access | Personal Training | Tanning | Group Exercise</p>
  <div class="brand"><span class="brand__dot"></span>Bold Pace Fitness</div>
</section>

<!-- Small windows spelling RESULTS -->
<section class="window window--small" style="left:27px">
  <svg viewBox="0 0 158 197"><text class="letter" x="31" y="148" font-size="138" textLength="96" lengthAdjust="spacingAndGlyphs" fill="url(#tone-group)" role="img" aria-label="Letter R filled with a group exercise photo">R</text></svg>
  <div class="rule"></div>
  <div class="brand"><span class="brand__dot"></span>Bold Pace Fitness</div>
</section>
<section class="window window--small" style="left:191px">
  <svg viewBox="0 0 158 197"><text class="letter" x="37" y="148" font-size="138" textLength="84" lengthAdjust="spacingAndGlyphs" fill="url(#tone-weights)" role="img" aria-label="Letter E filled with a weight training photo">E</text></svg>
  <div class="rule"></div>
  <div class="brand"><span class="brand__dot"></span>Bold Pace Fitness</div>
</section>
<section class="window window--small" style="left:355px">
  <svg viewBox="0 0 158 197"><text class="letter" x="34" y="148" font-size="138" textLength="91" lengthAdjust="spacingAndGlyphs" fill="url(#tone-cycling)" role="img" aria-label="Letter S filled with a spin class photo">S</text></svg>
  <div class="rule"></div>
  <div class="brand"><span class="brand__dot"></span>Bold Pace Fitness</div>
</section>
<section class="window window--small" style="left:518px">
  <svg viewBox="0 0 158 197"><text class="letter" x="32" y="148" font-size="138" textLength="94" lengthAdjust="spacingAndGlyphs" fill="url(#tone-kettlebell)" role="img" aria-label="Letter U filled with a kettlebell workout photo">U</text></svg>
  <div class="rule"></div>
  <div class="brand"><span class="brand__dot"></span>Bold Pace Fitness</div>
</section>
<section class="window window--small" style="left:682px">
  <svg viewBox="0 0 158 197"><text class="letter" x="40" y="148" font-size="138" textLength="76" lengthAdjust="spacingAndGlyphs" fill="url(#tone-treadmill)" role="img" aria-label="Letter L filled with a cardio machine photo">L</text></svg>
  <div class="rule"></div>
  <div class="brand"><span class="brand__dot"></span>Bold Pace Fitness</div>
</section>
<section class="window window--small" style="left:845px">
  <svg viewBox="0 0 158 197"><text class="letter" x="30" y="148" font-size="138" textLength="96" lengthAdjust="spacingAndGlyphs" fill="url(#tone-friends)" role="img" aria-label="Letter T filled with a photo of two women friends at the gym">T</text></svg>
  <div class="rule"></div>
  <div class="brand"><span class="brand__dot"></span>Bold Pace Fitness</div>
</section>
<section class="window window--small" style="left:1009px">
  <svg viewBox="0 0 158 197"><text class="letter" x="34" y="148" font-size="138" textLength="91" lengthAdjust="spacingAndGlyphs" fill="url(#tone-trainer)" role="img" aria-label="Letter S filled with a photo of a personal trainer">S</text></svg>
  <div class="rule"></div>
  <div class="brand"><span class="brand__dot"></span>Bold Pace Fitness</div>
</section>
</body>
</html>
```